Cake Bakery needs Large New Vibrant Window Decals

Our cake bakery is moving to a new location. We want to place window decals (vinyl) on 7 separate windows that are all the same size. (Image is attached for your reference. The windows are the ones within the red outline.)

The windows are approximately 76 inches tall and 98 inches wide. We have uploaded an image of the storefront to show you the 7 windows that need be to covered.

There are also 2 side by side doors that need a decals too. We have uploaded a logo we are using. You are allowed to change the logo color to better coordinate with a design you can create.

We want the colors to be bright and cheerful. You can see our current bakery website at brindlewickpastry.com. ( I included the sign above our bakery if that helps you.)

Do not use any images of cakes or other bakery products in your design.

The graphics can be simple and clean or can be vivid and loud. We will consider all concepts.

You can create one design to be duplicated for each window or create a design that would flow across all the windows in a landscape effect.

Target Market(s)

People who purchase cakes for any occasion.

Industry/Entity Type

Bakery

Requirements
Must have
• Must have the logo on each window
Nice to have
• Open to any concepts
Should not have
• No images of cakes or other bakery products. The graphics must stand the test of time for the next 10 years.

```html
<!DOCTYPE html>
<html lang="en">
<head>
<meta charset="utf-8">
<title>Brindlewick Pastry – Window Decal</title>
<link href="https://fonts.googleapis.com/css2?family=Fredoka:wght@600&display=swap" rel="stylesheet">
<style>
  :root {
    --backdrop: #f4f1ee;
    --stripe-light: #fcd9c8;
    --stripe-dark: #f8c6ae;
    --brand-coral: #e9566a;
    --edge-line: #ef8f86;
  }
  * { margin: 0; padding: 0; box-sizing: border-box; }
  html, body {
    width: 1200px;
    height: 1000px;
    overflow: hidden;
    background: var(--backdrop);
  }
  .canvas {
    width: 1200px;
    height: 1000px;
    display: flex;
    align-items: center;
    justify-content: center;
  }
  .window-decal {
    position: relative;
    width: 1000px;
    height: 776px;
    background: repeating-linear-gradient(
      90deg,
      var(--stripe-light) 0 62px,
      var(--stripe-dark) 62px 124px
    );
    border: 3px solid var(--edge-line);
    display: flex;
    align-items: center;
    justify-content: center;
  }
  .window-decal__edge {
    position: absolute;
    left: 0;
    right: 0;
    bottom: 22px;
    height: 0;
    border-top: 6px dotted var(--edge-line);
  }
  .brand-name {
    display: flex;
    align-items: center;
    gap: 22px;
    font-family: "Fredoka", sans-serif;
    font-weight: 600;
    font-size: 104px;
    line-height: 1;
    color: var(--brand-coral);
    text-align: center;
  }
  .brand-name__dot {
    width: 34px;
    height: 34px;
    border-radius: 50%;
    background: var(--brand-coral);
    flex: none;
  }
</style>
</head>
<body>
  <main class="canvas">
    <section class="window-decal" aria-label="Striped window decal with bakery name">
      <div class="brand-name">
        <span class="brand-name__dot"></span>
        <span class="brand-name__text">Brindlewick Pastry</span>
      </div>
      <div class="window-decal__edge"></div>
    </section>
  </main>
</body>
</html>
```